Creat new BusinessCard for Brightpath Advisory!

Hello Creativ Designer. I need a new Businesscard for our brand new Company "Brightpath Coaching". We do Consulting for a better Life & Work Situation. to create Fulfillment, Sense, Motivation and healthy Work Places in Company's. So we try to create a better World and help the employee to like what they do!
So we would like to have 2 Sites on the card. On the Back we want to put this words: "The sole meaning of life, is to serve humanity" (it can be vertical oder horizontal). In the front there is the Logo (Black or White) and Adress+ and Slogan.

Slogan on the front: -Make your Business & Life to a better place-

Name: Lukas Fenwald
Titel: Founder - Visionary - Trainer
Adress: Based in Switzerland

Tel: +41 (0) 71 483 27 15
Email: hello@brightpath-coaching.ch
Homepage: www.brightpath-coaching.ch

Thanks for your inspired Ideas and your help to make the world to a better place! IT has to be ready to print and normal Size.

Target Market(s)

insurance, Bank, Telecom, industry, IT, Medical

Contact Information for Business Card

Breite: 85 mm x Höhe: 55 mm

Colors

Designer to choose colors to be used in the design.

Requirements
Nice to have
• Thanks for your Ideas so far!
• Maybe you can try/play with the colors: Purple Code #652C8F and Grey #979797 from the Zorvik Logo purple and grey (but only a soft combination, not to much)

```html
<!DOCTYPE html>
<html lang="en">
<head>
<meta charset="utf-8">
<title>Brightpath Coaching – Business Card</title>
<link rel="stylesheet" href="https://fonts.googleapis.com/css2?family=Questrial&family=Raleway:wght@400;600;700&display=swap">
<style>
  :root {
    --stage: #3a3f47;
    --card-white: #ffffff;
    --card-black: #141414;
    --ink: #111111;
    --grey: #979797;
    --grey-light: #a9a9a9;
    --purple: #652c8f;
    --white: #ffffff;
  }
  * { box-sizing: border-box; margin: 0; padding: 0; }
  html, body { width: 1200px; height: 900px; overflow: hidden; }
  body {
    background: var(--stage);
    position: relative;
    font-family: "Raleway", sans-serif;
  }
  .card {
    position: absolute;
    top: 276px;
    width: 540px;
    height: 349px;
    border-radius: 4px;
    overflow: hidden;
    box-shadow: 0 12px 30px rgba(0,0,0,.35);
  }

  /* Front side */
  .card-front { left: 30px; background: var(--card-white); }
  .holder-name {
    position: absolute; left: 34px; top: 38px;
    font-weight: 700; font-size: 22px; letter-spacing: .5px;
    color: var(--ink); text-transform: uppercase;
  }
  .holder-title {
    position: absolute; left: 34px; top: 68px;
    font-size: 15px; letter-spacing: 1px; color: var(--grey);
    text-transform: uppercase;
  }
  .contact-list {
    position: absolute; left: 34px; top: 162px;
    list-style: none; font-size: 13px; color: var(--ink);
  }
  .contact-list li { display: flex; align-items: center; gap: 8px; height: 22px; }
  .contact-list svg { width: 12px; height: 12px; fill: var(--ink); }
  .brand-block {
    position: absolute; left: 290px; top: 118px; width: 220px;
    text-align: center;
  }
  .brand-dot {
    width: 64px; height: 64px; border-radius: 50%;
    background: var(--ink); margin: 0 auto 12px;
  }
  .brand-name {
    font-weight: 700; font-size: 22px; color: var(--ink);
    text-transform: uppercase; letter-spacing: 1px;
    border-top: 1px solid var(--ink); border-bottom: 1px solid var(--ink);
    padding: 4px 0;
  }
  .brand-location {
    margin-top: 10px; font-size: 13px; color: var(--ink);
  }
  .slogan-band {
    position: absolute; left: 0; right: 0; top: 286px; height: 34px;
    background: var(--purple); color: var(--white);
    font-size: 15px; display: flex; align-items: center; padding-left: 34px;
  }

  /* Back side */
  .card-back { left: 630px; background: var(--card-black); font-family: "Questrial", sans-serif; color: var(--white); }
  .quote { position: absolute; left: 0; top: 0; width: 100%; height: 100%; }
  .quote span { position: absolute; line-height: 1; white-space: nowrap; }
  .q-the { left: 214px; top: 58px; font-size: 15px; }
  .q-sole { left: 246px; top: 40px; font-size: 46px; }
  .q-of { left: 58px; top: 130px; font-size: 24px; }
  .q-life { left: 88px; top: 86px; font-size: 96px; color: var(--grey-light); letter-spacing: -3px; }
  .q-isto { left: 228px; top: 150px; font-size: 20px; }
  .q-serve { left: 286px; top: 102px; font-size: 86px; font-weight: 700; letter-spacing: -1px; }
  .q-humanity { left: 84px; top: 188px; font-size: 84px; color: var(--purple); letter-spacing: -1px; }
  .q-url { left: 92px; top: 292px; font-size: 14px; }
</style>
</head>
<body>

<section class="card card-front" aria-label="Business card front">
  <h1 class="holder-name">Lukas Fenwald</h1>
  <p class="holder-title">Founder - Visionary - Trainer</p>

  <ul class="contact-list">
    <li>
      <svg viewBox="0 0 24 24" aria-hidden="true"><path d="M6.6 10.8a15.1 15.1 0 0 0 6.6 6.6l2.2-2.2a1 1 0 0 1 1-.25 11.4 11.4 0 0 0 3.6.57 1 1 0 0 1 1 1V20a1 1 0 0 1-1 1A17 17 0 0 1 3 4a1 1 0 0 1 1-1h3.5a1 1 0 0 1 1 1c0 1.25.2 2.45.57 3.57a1 1 0 0 1-.25 1z"/></svg>
      +41 (0) 71 483 27 15
    </li>
    <li>
      <svg viewBox="0 0 24 24" aria-hidden="true"><path d="M2 5h20v14H2z M4 7v.5l8 5 8-5V7l-8 5z" fill-rule="evenodd"/></svg>
      hello@brightpath-coaching.ch
    </li>
    <li>
      <svg viewBox="0 0 24 24" aria-hidden="true"><path d="M12 2a10 10 0 1 0 0 20 10 10 0 0 0 0-20zm7.9 9h-3.9a15 15 0 0 0-1.4-6.3A8 8 0 0 1 19.9 11zM12 4c1 1.3 1.9 3.8 2 7h-4c.1-3.2 1-5.7 2-7zM9.4 4.7A15 15 0 0 0 8 11H4.1a8 8 0 0 1 5.3-6.3zM4.1 13H8a15 15 0 0 0 1.4 6.3A8 8 0 0 1 4.1 13zm7.9 7c-1-1.3-1.9-3.8-2-7h4c-.1 3.2-1 5.7-2 7zm2.6-.7A15 15 0 0 0 16 13h3.9a8 8 0 0 1-5.3 6.3z"/></svg>
      www.brightpath-coaching.ch
    </li>
  </ul>

  <div class="brand-block">
    <div class="brand-dot" aria-hidden="true"></div>
    <p class="brand-name">Brightpath Coaching</p>
    <p class="brand-location">Based in Switzerland</p>
  </div>

  <p class="slogan-band">Make your Business &amp; Life to a better place</p>
</section>

<section class="card card-back" aria-label="Business card back">
  <p class="quote">
    <span class="q-the">The</span>
    <span class="q-sole">sole meaning</span>
    <span class="q-of">of</span>
    <span class="q-life">life</span>
    <span class="q-isto">is to</span>
    <span class="q-serve">serve</span>
    <span class="q-humanity">humanity</span>
    <span class="q-url">www.brightpath-coaching.ch</span>
  </p>
</section>

</body>
</html>
```